Poster design for The Dorrable Co.

Create a poster that will sell our company, all the information needed is on our website @ thedorrableco.co.uk
Creative design is down to you.

I have attached the AI for our logo.

```html
<!DOCTYPE html>
<html lang="en">
<head>
<meta charset="utf-8">
<title>The Dorrable Co. — Poster</title>
<link href="https://fonts.googleapis.com/css2?family=Hind:wght@300;400;500&display=swap" rel="stylesheet">
<style>
  :root {
    --brand-red: #9b0c12;
    --band-grey: #6d6e70;
    --footer-grey: #e0e1e3;
    --text-grey: #6d6e70;
    --white: #ffffff;
  }
  * { margin: 0; padding: 0; box-sizing: border-box; }
  html, body {
    width: 849px;
    height: 1200px;
    overflow: hidden;
    background: var(--footer-grey);
  }
  .poster {
    position: relative;
    width: 849px;
    height: 1200px;
    font-family: "Hind", Arial, sans-serif;
    overflow: hidden;
  }
  .hero {
    position: absolute;
    left: 0; top: 0;
    width: 849px;
    height: 884px;
    background: var(--brand-red);
  }
  .headline {
    position: absolute;
    left: 0; top: 0;
    width: 849px;
    height: 600px;
  }
  .headline text {
    fill: var(--white);
    font-family: "Hind", Arial, sans-serif;
    font-weight: 300;
  }
  .services {
    position: absolute;
    left: 0;
    top: 585px;
    width: 849px;
    list-style: none;
    text-align: center;
    color: var(--white);
    font-size: 25px;
    font-weight: 400;
    line-height: 34.5px;
    letter-spacing: 0.3px;
  }
  .divider-band {
    position: absolute;
    left: 0; top: 884px;
    width: 849px;
    height: 14px;
    background: var(--band-grey);
  }
  .footer {
    position: absolute;
    left: 0; top: 898px;
    width: 849px;
    height: 302px;
    background: var(--footer-grey);
  }
  .brand-mark {
    position: absolute;
    left: 164px;
    top: 72px;
    width: 52px;
    height: 52px;
    border-radius: 50%;
    background: var(--brand-red);
  }
  .brand-rule {
    position: absolute;
    left: 294px;
    top: 34px;
    width: 2px;
    height: 134px;
    background: var(--band-grey);
  }
  .brand-name {
    position: absolute;
    left: 334px;
    top: 72px;
    color: var(--brand-red);
    font-size: 55px;
    font-weight: 500;
    line-height: 1;
    white-space: nowrap;
  }
  .brand-tagline {
    position: absolute;
    left: 390px;
    top: 128px;
    width: 272px;
    color: var(--text-grey);
    font-size: 17px;
    font-weight: 400;
    line-height: 1;
    text-align: center;
    white-space: nowrap;
  }
  .contact {
    position: absolute;
    left: 0;
    top: 192px;
    width: 849px;
    font-style: normal;
    text-align: center;
    color: var(--text-grey);
    font-size: 15px;
    font-weight: 400;
    line-height: 20px;
  }
</style>
</head>
<body>
  <main class="poster">
    <section class="hero">
      <svg class="headline" viewBox="0 0 849 600" aria-label="Simple Smart Beautiful">
        <text x="40" y="212" font-size="240" textLength="768" lengthAdjust="spacingAndGlyphs">SIMPLE</text>
        <text x="40" y="410" font-size="240" textLength="768" lengthAdjust="spacingAndGlyphs">SMART</text>
        <text x="38" y="544" font-size="160" textLength="772" lengthAdjust="spacingAndGlyphs">BEAUTIFUL</text>
      </svg>
      <ul class="services">
        <li>WEBSITE DESIGN</li>
        <li>DOMAIN NAMES</li>
        <li>LOGO DESIGN</li>
        <li>WEBSITE HOSTING</li>
        <li>DOMAIN LINKED EMAIL ACCOUNTS</li>
        <li>WEBSITE MANAGEMENT</li>
        <li>PHOTOGRAPHY</li>
        <li>GRAPHIC STOCK</li>
      </ul>
    </section>
    <div class="divider-band"></div>
    <footer class="footer">
      <span class="brand-mark" aria-hidden="true"></span>
      <span class="brand-rule" aria-hidden="true"></span>
      <h1 class="brand-name">The Dorrable Co.</h1>
      <p class="brand-tagline">SIMPLE, SMART AND BEAUTIFUL</p>
      <address class="contact">
        24 Orchard Lane, Hollowby, Leicestershire, LE9 4QT<br>
        Phone: 07700900462<br>
        Email: info@thedorrableco.co.uk<br>
        www.thedorrableco.co.uk
      </address>
    </footer>
  </main>
</body>
</html>
```